wolterhagen.info (Physiotherapeut)   //   quellbrand-athletic Webseite
wolterhagen.info (Physiotherapeut) // quellbrand-athletic Webseite
Zielgruppe
Die angesprochene Zielgruppe ist sportlich unterwegs (Sportler jeglicher Sportrichtung). Der externe Shop geht in Richtung Apparels / Kleidung.
Vielleicht wird es aber auch nur eine Physio-Seite und die Apparels kommen im zweiten Schritt - das liegt am Design das man mir präsentiert .... Also legt los ...
(KELVARO wird HOST)
Aufgabenstellung
Mein Name ist Jonathan Wolterhagen ich bin Physiotherapeut / Osteopath (etc).
Die Domain www.wolterhagen.info gehört mir und es würde auch für den Anfang reichen eine digitale Visitenkarte von mir zu erstellen ...
Weiter möchte ich eine Webseite mit dem Namen "quellbrand-athletic" eröffnen. [COM/DE]
Die zu kreierenden Seiten innerhalb der Domain quellbrand-athleti sind:
Main-/LandingPage,
ShopPage (Weiterleitung zu einer externen Webseite),
Impressum,
KooperationsPage (andere Projekte bzw. Webseiten von mir, die in Zukunft kommen).
Design-Vorschläge und umsetzbare / hochladbare Pages (KELVARO) oder NUR Grafiken sind gerne gesehen ...
Die angesprochene Zielgruppe ist sportlich unterwegs (Sportler jeglicher Sportrichtung). Der externe Shop geht in Richtung Apparels.
Die angesprochenen Kreaturen brauchen ein Heim, dass durch ein Schloss repräsentiert werden soll. Evtl. ein Labor. Nicht zu kindlich! Nicht zu düster oder blutig.
Was ich möchte ist: Corporate Identity, eine Webpage (host der Domain wird KELVARO), Logo, etc
Zweiter Schritt wird sein: Grafiken für die Apparels / Klamotten.

```html
<!DOCTYPE html>
<html lang="en">
<head>
<meta charset="utf-8">
<title>wolterhagen – Physiotherapeut</title>
<link rel="stylesheet" href="https://fonts.googleapis.com/css2?family=Cabin:wght@400;600;700&family=Josefin+Sans:wght@300&family=Quicksand:wght@400&display=swap">
<style>
:root{
  --green:#3bbd45;
  --green-band:#43c14c;
  --green-footer:#34b23d;
  --green-footer-top:#45c04d;
  --green-dark:#2a9932;
  --green-ink:#1f6e25;
  --hero-bg:#efefe9;
  --ink:#6f6f6f;
  --ink-dark:#3c3c3c;
  --rule:#d6d6d0;
  --white:#ffffff;
}
*{box-sizing:border-box;margin:0;padding:0}
html,body{width:1024px;height:1200px;overflow:hidden;background:var(--white)}
body{position:relative;font-family:"Cabin",sans-serif;color:var(--ink)}
.topline{position:absolute;left:0;top:0;width:1024px;height:4px;background:var(--green)}
.brand{position:absolute;top:26px;left:0;width:1024px;text-align:center}
.brand-name{font-weight:600;font-size:20px;color:var(--green);line-height:1}
.brand-tag{font-size:5px;letter-spacing:3.6px;color:var(--green);margin-top:2px}

.hero{position:absolute;left:0;top:76px;width:1024px;height:397px;background:var(--hero-bg);overflow:hidden}
.hero-photo{position:absolute;left:480px;top:0;width:544px;height:397px;
  background:
   linear-gradient(90deg,rgba(239,239,233,1) 0%,rgba(239,239,233,0) 28%),
   linear-gradient(90deg,rgba(0,0,0,0) 55%,#b8795c 72%,#8a3f25 100%),
   linear-gradient(180deg,#8fa37c 0%,#c2c4bb 45%,#d4d3ce 100%);}
.nav{position:absolute;left:0;top:0;width:1024px;height:52px;background:rgba(205,200,192,.85);border-top:2px solid #bdb8b0;border-bottom:2px solid #bdb8b0}
.nav a{position:absolute;top:20px;font-weight:600;font-size:8px;color:#7e7a72;text-decoration:none}
.nav a.active{color:var(--ink-dark)}
.nav .underline{position:absolute;left:350px;bottom:-2px;width:68px;height:3px;background:#4d4a45}
.hero-title{position:absolute;left:187px;top:112px;font-family:"Josefin Sans",sans-serif;font-weight:300;font-size:26px;letter-spacing:3.4px;color:var(--green);white-space:nowrap}
.hero-rule{position:absolute;left:180px;top:150px;width:395px;height:1px;background:var(--rule)}
.hero-copy{position:absolute;left:189px;top:177px;width:350px;font-family:"Quicksand",sans-serif;font-size:8.4px;line-height:10.8px;color:#7f7f7a}
.hero-copy p{margin-bottom:11px}
.follow{position:absolute;left:193px;top:357px;display:flex;align-items:center;gap:10px;font-size:8px;font-weight:600;color:#a9a9a2}
.follow .dot{width:22px;height:22px;border-radius:50%;background:var(--green)}

.notch{position:absolute;left:504px;top:472px;width:0;height:0;border-left:8px solid transparent;border-right:8px solid transparent;border-top:13px solid var(--hero-bg);z-index:3}

.contact-band{position:absolute;left:0;top:473px;width:1024px;height:140px;background:linear-gradient(90deg,#5fcf63 0%,var(--green-band) 45%,#5cc95f 100%);overflow:hidden}
.band-photo{position:absolute;left:0;top:0;width:260px;height:140px;background:linear-gradient(90deg,#4aa650 0%,#5ab95e 60%,rgba(67,193,76,0) 100%)}
.contact-item{position:absolute;top:45px;display:flex;align-items:center;gap:24px;color:var(--white);font-size:8.6px;font-weight:600;line-height:15px;white-space:nowrap}
.contact-item svg{width:48px;height:48px;flex:none}

.section-head{position:absolute;left:165px;top:646px;width:697px;display:flex;align-items:center;gap:14px}
.section-head .line{flex:1;height:1px;background:#d7ecd7}
.section-head h2{font-family:"Josefin Sans",sans-serif;font-weight:300;font-size:26px;letter-spacing:1.5px;color:var(--green)}
.columns{position:absolute;left:185px;top:711px;width:667px;display:flex;gap:40px}
.columns .col{width:312px;font-size:10.4px;line-height:12.6px;color:#7a7a7a}
.columns p{margin-bottom:12.6px}

.footer{position:absolute;left:0;top:1075px;width:1024px;height:98px;background:var(--green-footer);border-top:5px solid var(--green-footer-top)}
.footer-label{position:absolute;left:232px;top:41px;display:flex;align-items:center;gap:6px;font-weight:700;font-size:10px;color:var(--green-ink)}
.footer-contact{position:absolute;left:348px;top:34px;font-size:8.6px;line-height:13.5px;color:var(--white)}
.footer-mark{position:absolute;left:612px;top:36px;width:22px;height:22px;border-radius:50%;border:2px solid var(--white)}
.footer-copy{position:absolute;left:694px;top:35px;font-size:8.6px;font-weight:600;line-height:11.5px;color:var(--white)}
.subnav{position:absolute;left:0;top:1173px;width:1024px;height:27px;background:var(--green-dark)}
.subnav a{position:absolute;top:9px;font-size:7px;font-weight:700;color:var(--green-ink);text-decoration:none}
</style>
</head>
<body>
<div class="topline"></div>
<header class="brand">
  <div class="brand-name">wolterhagen</div>
  <div class="brand-tag">Physiotherapeut</div>
</header>

<section class="hero">
  <div class="hero-photo" role="img" aria-label="Photo of a runner with red hair seen from behind on a tree-lined running track"></div>
  <nav class="nav">
    <a class="active" style="left:370px">HOME</a>
    <a style="left:447px">SHOP</a>
    <a style="left:514px">COOPERATION</a>
    <a style="left:605px">CONTACT US</a>
    <span class="underline"></span>
  </nav>
  <h1 class="hero-title">LOREM IPSUM DOLOR AMET</h1>
  <div class="hero-rule"></div>
  <div class="hero-copy">
    <p>Lorem ipsum ad his scripta blandit partiendo eum fastidii accumsan euripidis in, eum liber hendrerit an.</p>
    <p>Ut wisisuscipiantur, quo dicit ridens inciderint iduo mundi lobortis refor midans eu, legimus senserit definie an eos, eu sit tincidunt incorru definitionem, vis mutat affert percipit.</p>
    <p>Lorem ipsum ad his scripta blandit partiendo, eum fastidii accumsan euripidis in, eum liber hendrerit an. Qui ut wisi suscipiantur, quo dicit ridens inciderint id. Quo mundi lobortis reformidans eu, legimus senserit definiebas an eos, eu sit tincidunt incorrupte definitionem, vis mutat affert percipit.</p>
  </div>
  <div class="follow">
    <span>Follow us:</span>
    <span class="dot" role="img" aria-label="Social network link"></span>
    <span class="dot" role="img" aria-label="Social network link"></span>
  </div>
</section>
<div class="notch"></div>

<section class="contact-band">
  <div class="band-photo" role="img" aria-label="Photo of a cyclist in a helmet"></div>
  <div class="contact-item" style="left:235px">
    <svg viewBox="0 0 50 50"><circle cx="25" cy="25" r="23" fill="none" stroke="#fff" stroke-width="2"/><path d="M25 13a8 8 0 0 0-8 8c0 6 8 15 8 15s8-9 8-15a8 8 0 0 0-8-8z" fill="#fff"/><circle cx="25" cy="21" r="3" fill="#43c14c"/></svg>
    <span>Harbor Lane N #4820,<br>City Country</span>
  </div>
  <div class="contact-item" style="left:460px">
    <svg viewBox="0 0 50 50"><circle cx="25" cy="25" r="23" fill="none" stroke="#fff" stroke-width="2"/><path d="M21 14l4 5-2.5 3c1.5 3 3.5 5 6 6.5l3-2.5 5 4-3 4c-8-1-15-8-16-16z" fill="#fff"/></svg>
    <span>+561-40718293</span>
  </div>
  <div class="contact-item" style="left:650px">
    <svg viewBox="0 0 50 50"><circle cx="25" cy="25" r="23" fill="none" stroke="#fff" stroke-width="2"/><rect x="14" y="17" width="22" height="16" fill="none" stroke="#fff" stroke-width="2"/><path d="M17 22h16M17 26h16M17 30h16" stroke="#fff" stroke-width="1.5"/></svg>
    <span>email@wolterhagen-physio.com</span>
  </div>
</section>

<section>
  <div class="section-head"><span class="line"></span><h2>LOREM SIT</h2><span class="line"></span></div>
  <div class="columns">
    <div class="col">
      <p>Lorem ipsum ad his scripta blandit partiendo eum fastidii accumsan euripidis in, eum liber hendrerit an ut wisisuscipiantur, quo dicit ridens inciderint id. Quo mundi lobortis refor midans eu, legimus senserit definie an eos, eu sit tincidunt incorru definitionem, vis mutat affert percipit.</p>
      <p>Ad his scripta blandit partiendo eum fastidii accumsan euripidis in, eum liber hendrerit an ut wisisuscipiantur, quo dicit ridens inciderint id. Quo mundi lobortis refor midans eu, legimus senserit definie an eos, eu sit tincidunt incorru definitionem, vis mutat affert percipit ipsum ad his scripta blandit partiendo eum fastidii accumsan euripidis in, eum liber hendrerit an ut wisisuscipiantur, quo dicit ridens inciderint id. Quo mundi lobortis refor midans eu, legimus senserit definie an eos, eu sit tincidunt incorru definitionem, vis mutat affert percipit.</p>
      <p>Lorem ipsum ad his scripta blandit partiendo eum fastidii accumsan euripidis in, eum liber hendrerit an ut wisisuscipiantur, quo dicit ridens inciderint id. Quo mundi lobortis refor midans eu, legimus senserit definie an eos, eu sit tincidunt incorru definitionem, vis mutat affert percipit.</p>
      <p>Scripta blandit partiendo eum fastidii accumsan euripidis in, eum liber hendrerit an ut wisisuscipiantur, quo dicit ridens inciderint id. Quo mundi lobortis refor midans eu, legimus senserit definie an eos, eu sit tincidunt incorru definitionem, vis mutat affert percipit.</p>
    </div>
    <div class="col">
      <p>Lorem ipsum ad his scripta blandit partiendo eum fastidii accumsan euripidis in, eum liber hendrerit an ut wisisuscipiantur, quo dicit ridens inciderint id. Quo mundi lobortis refor midans eu, legimus senserit definie an eos, eu sit tincidunt incorru definitionem, vis mutat affert percipit.</p>
      <p>Ad his scripta blandit partiendo eum fastidii accumsan euripidis in, eum liber hendrerit an ut wisisuscipiantur, quo dicit ridens inciderint id. Quo mundi lobortis refor midans eu, legimus senserit definie an eos, eu sit tincidunt incorru definitionem, vis mutat affert percipit ipsum ad his scripta blandit partiendo eum fastidii accumsan euripidis in, eum liber hendrerit an ut wisisuscipiantur, quo dicit ridens inciderint id. Quo mundi lobortis refor midans eu, legimus senserit definie an eos, eu sit tincidunt incorru definitionem, vis mutat affert percipit.</p>
      <p>Lorem ipsum ad his scripta blandit partiendo eum fastidii accumsan euripidis in, eum liber hendrerit an ut wisisuscipiantur, quo dicit ridens inciderint id. Quo mundi lobortis refor midans eu, legimus senserit definie an eos, eu sit tincidunt incorru definitionem, vis mutat affert percipit.</p>
      <p>Scripta blandit partiendo eum fastidii accumsan euripidis in, eum liber hendrerit an ut wisisuscipiantur, quo dicit ridens inciderint id. Quo mundi lobortis refor midans eu, legimus senserit definie an eos, eu sit tincidunt incorru definitionem, vis mutat affert percipit.</p>
    </div>
  </div>
</section>

<footer class="footer">
  <div class="footer-label">
    <svg width="9" height="12" viewBox="0 0 9 12"><path d="M4.5 1a3.5 3.5 0 0 0-3.5 3.5C1 7 4.5 11 4.5 11S8 7 8 4.5A3.5 3.5 0 0 0 4.5 1z" fill="none" stroke="#1f6e25" stroke-width="1.2"/></svg>
    <span>CONTACT US :</span>
  </div>
  <div class="footer-contact">email@wolterhagen-physio.com<br>Phone: 866-504-7390</div>
  <div class="footer-mark"></div>
  <div class="footer-copy">Copyright wolterhagen<br>2015. All rights reserved.</div>
</footer>
<nav class="subnav">
  <a style="left:395px">HOME</a>
  <a style="left:448px">SHOP</a>
  <a style="left:497px">COOPERATION</a>
  <a style="left:583px">CONTACT US</a>
</nav>
</body>
</html>
```